Coverneugestaltung einer Zeitschrift für Betroffene mit Allergien
Zielgruppe
Wir sind ein medizinischer Verlag und geben Patientenzeitschriften heraus. Das Magazin 'Pollenta' richtet sich an Betroffene mit Allergien, Nahrungsmittelunverträglichkeiten, Lungen- und Hauterkrankungen
Aufgabenstellung
Das Cover sollte modern und seriös wirken. Die rote Ecke unten rechts "Ihr Exemplar zum Mitnehmen" muss zwingend unten rechts übernommen werden. Die Covergestaltung sollte so sein, dass zukünftig verschiedene Titelbilder verwendet werden können (u.a. Freisteller). Die Zeitschrift "Pollenta" erscheint viermal im Jahr.
Es darf alles verändert werden, Schrift, Farbe, Wort-Bild-Marke etc. Wir sind hier offen für Neues.

```html
<!DOCTYPE html>
<html lang="de">
<head>
<meta charset="utf-8">
<title>Pollenta – Cover</title>
<link href="https://fonts.googleapis.com/css2?family=Montserrat:wght@400;600;700;800&display=swap" rel="stylesheet">
<style>
  :root {
    --stage: #e6e6e6;
    --paper: #ffffff;
    --brand-blue: #2c3a92;
    --text-grey: #555b66;
    --leaf-dark: #2f5a1e;
    --leaf-mid: #5f9434;
    --leaf-light: #a9c96a;
    --denim: #b9c3cf;
    --shirt: #d8292c;
  }
  * { box-sizing: border-box; margin: 0; padding: 0; }
  html, body { width: 1200px; height: 900px; overflow: hidden; }
  body {
    background: var(--stage);
    font-family: "Montserrat", Arial, sans-serif;
    position: relative;
  }
  .cover {
    position: absolute;
    left: 300px; top: 26px;
    width: 600px; height: 848px;
    overflow: hidden;
    background: var(--paper);
    box-shadow: 0 4px 18px rgba(0,0,0,.18);
  }
  .cover-photo {
    position: absolute; inset: 0;
    background:
      radial-gradient(ellipse 38% 30% at 55% 48%, var(--shirt) 0%, rgba(216,41,44,.75) 45%, rgba(216,41,44,0) 100%),
      radial-gradient(ellipse 40% 26% at 62% 16%, var(--denim) 0%, rgba(185,195,207,0) 100%),
      radial-gradient(ellipse 30% 22% at 62% 72%, #e9c9a4 0%, rgba(233,201,164,0) 100%),
      linear-gradient(160deg, var(--leaf-dark) 0%, var(--leaf-mid) 45%, var(--leaf-light) 100%);
  }
  .masthead {
    position: absolute; left: 0; top: 0;
    width: 360px; height: 128px;
    background: var(--paper);
    clip-path: polygon(0 0, 100% 0, 100% 62%, 88% 100%, 0 100%);
    padding: 26px 0 0 34px;
  }
  .brand-name {
    display: flex; align-items: center; gap: 10px;
    font-weight: 800; font-size: 50px; letter-spacing: -1px;
    color: var(--brand-blue); line-height: 1;
  }
  .brand-dot {
    width: 14px; height: 14px; border-radius: 50%;
    background: var(--brand-blue);
  }
  .brand-claim {
    margin-top: 8px;
    font-size: 11px; font-weight: 400; color: var(--text-grey);
  }
  .issue-label {
    position: absolute; right: 22px; top: 18px;
    font-size: 9px; font-weight: 600; color: var(--paper);
  }
  .teaser {
    position: absolute;
    background: var(--paper);
    padding: 14px 28px 14px 36px;
    clip-path: polygon(0 50%, 14px 0, 100% 0, 100% 100%, 14px 100%);
  }
  .teaser.left {
    padding: 14px 36px 14px 22px;
    clip-path: polygon(0 0, calc(100% - 14px) 0, 100% 50%, calc(100% - 14px) 100%, 0 100%);
  }
  .teaser-title {
    font-weight: 700; font-size: 24px; line-height: 1.05;
    text-transform: uppercase; color: var(--brand-blue);
  }
  .teaser-sub {
    margin-top: 4px;
    font-size: 13px; font-weight: 400; color: var(--text-grey);
  }
  .teaser-research { right: 0; top: 392px; }
  .teaser-heights { left: 0; top: 596px; }
  .teaser-cold { left: 0; top: 708px; }
  .takeaway-corner {
    position: absolute; right: 0; bottom: 0;
    width: 150px; height: 150px;
  }
  .takeaway-text {
    position: absolute; right: 10px; bottom: 18px;
    width: 92px;
    font-size: 10px; font-weight: 600; line-height: 1.25;
    color: var(--paper); text-align: right;
  }
</style>
</head>
<body>
  <article class="cover">
    <div class="cover-photo" role="img" aria-label="Titelfoto: Mädchen im roten T-Shirt hängt kopfüber im Baum vor grünem Laub"></div>

    <header class="masthead">
      <div class="brand-name"><span>pollenta</span><span class="brand-dot"></span></div>
      <p class="brand-claim">Ihr Fach-Magazin für Allergien, Haut und Lunge</p>
    </header>
    <p class="issue-label">Ausgabe 2/2019</p>

    <section class="teaser teaser-research">
      <h2 class="teaser-title">Neue Hoffnung<br>in der Forschung</h2>
      <p class="teaser-sub">Den Lebensmut wiederfinden</p>
    </section>

    <section class="teaser left teaser-heights">
      <h2 class="teaser-title">Hoch hinaus<br>trotz Allergie</h2>
      <p class="teaser-sub">Den Lebensmut wiederfinden</p>
    </section>

    <section class="teaser left teaser-cold">
      <h2 class="teaser-title">Ein Schnupfen-<br>viele Ursachen</h2>
      <p class="teaser-sub">Den Lebensmut wiederfinden</p>
    </section>

    <svg class="takeaway-corner" viewBox="0 0 150 150" aria-hidden="true">
      <polygon points="150,0 150,150 0,150" fill="var(--brand-blue)"/>
    </svg>
    <p class="takeaway-text">Ihr Exemplar<br>zum Mitnehmen</p>
  </article>
</body>
</html>
```